Offshore Energy Projects Management Consultancy needs a business card design

Logo available. We provide teams to deliver engineering consultancy, project management and delivery teams mainly in the offshore renewables sector. The company is all about bringing the right people to a project to deliver the scope.

The business card will be used for all staff.

The business card should be quite simple, vibrant and uncluttered but convey experience, enthusiasm and integration.

Target Market(s)

Energy Project Developers and Tier 1 construction companies

Contact Information for Business Card

Logo should be on the back of the card. I'm happy for the designer to play with the colour of the logo and background colour.

Front of the card should convey all the must have information in a clear and professional manner but without being overly traditional.

Colors

Designer to choose colors to be used in the design.

Requirements
Must have
• Land Line Tel Number, Mobile Tel Number, Email, business address, web address.

```html
<!DOCTYPE html>
<html lang="en">
<head>
<meta charset="utf-8">
<title>Seaward Delivery Group – Business Card</title>
<link rel="stylesheet" href="https://fonts.googleapis.com/css2?family=Mulish:wght@400;600;700;800&display=swap">
<style>
  :root {
    --backdrop: #e9e6e1;
    --card-white: #f3f3f5;
    --brand-blue: #1174bd;
    --brand-sky: #29a9e0;
    --text-grey: #5f6062;
    --rule-grey: #8a8b8d;
    --white: #ffffff;
  }
  * { box-sizing: border-box; margin: 0; padding: 0; }
  html, body {
    width: 902px; height: 1200px; overflow: hidden;
    background: var(--backdrop);
    font-family: "Mulish", Arial, sans-serif;
  }
  .card {
    position: absolute;
    left: 78px; width: 744px; height: 436px;
    border-radius: 18px;
    overflow: hidden;
    box-shadow: 0 14px 24px rgba(0,0,0,0.18);
  }
  .card-front { top: 132px; background: var(--card-white); }
  .card-back { top: 636px; background: var(--brand-blue); }

  .front-brand {
    position: absolute; left: 62px; top: 208px; width: 290px;
    display: flex; align-items: center; justify-content: center; gap: 9px;
  }
  .brand-square { width: 15px; height: 15px; background: var(--brand-blue); flex: none; }
  .brand-name {
    font-weight: 800; font-size: 17px; letter-spacing: 0.3px;
    color: var(--text-grey); white-space: nowrap;
  }
  .divider {
    position: absolute; left: 378px; top: 110px;
    width: 1.5px; height: 213px; background: var(--rule-grey);
  }
  .contact { position: absolute; left: 450px; top: 104px; color: var(--text-grey); }
  .person-name { font-size: 30px; font-weight: 600; color: var(--brand-blue); line-height: 1.1; }
  .person-name .surname { color: var(--brand-sky); }
  .person-role { font-size: 17px; margin-top: 6px; }
  .contact-list { list-style: none; margin-top: 22px; }
  .contact-list li {
    display: flex; align-items: center; gap: 12px;
    font-size: 17px; line-height: 22.5px;
  }
  .contact-list svg { width: 13px; height: 13px; fill: var(--brand-blue); flex: none; }
  .address { font-size: 17px; line-height: 21px; margin-top: 14px; }

  .band { position: absolute; bottom: 0; height: 15px; }
  .band-dark { left: 0; width: 378px; background: var(--brand-blue); }
  .band-light { left: 380px; right: 0; background: var(--brand-sky); }

  .back-brand {
    position: absolute; inset: 0;
    display: flex; align-items: center; justify-content: center;
  }
  .back-brand .brand-name { color: var(--white); font-size: 30px; letter-spacing: 0.8px; }
</style>
</head>
<body>
  <section class="card card-front" aria-label="Card front">
    <div class="front-brand">
      <span class="brand-square" aria-hidden="true"></span>
      <span class="brand-name">SEAWARD DELIVERY GROUP</span>
    </div>
    <div class="divider"></div>
    <div class="contact">
      <h1 class="person-name">Daniel <span class="surname">Reyes</span></h1>
      <p class="person-role">CEO/ Founder</p>
      <ul class="contact-list">
        <li><svg viewBox="0 0 16 16" aria-hidden="true"><path d="M3.5 1l2.5 3-1.5 2c1 2 2.5 3.5 4.5 4.5l2-1.5 3 2.5-1.5 2.5C7 14 2 9 1 2.5z"/></svg>+44 7700 914362</li>
        <li><svg viewBox="0 0 16 16" aria-hidden="true"><path d="M1 5c2-3 12-3 14 0v2h-4V5.5H5V7H1z M3 8h10l1 6H2z"/></svg>+44 20 7946 0158</li>
        <li><svg viewBox="0 0 16 16" aria-hidden="true"><path d="M1 3h14L8 9z M1 4.5l7 5.5 7-5.5V13H1z"/></svg>d.reyes@seaward.example</li>
        <li><svg viewBox="0 0 16 16" aria-hidden="true"><circle cx="8" cy="8" r="7"/></svg>seawarddelivery</li>
      </ul>
      <p class="address">12th floor, Harbour Quay no<br>48 Tower North</p>
    </div>
    <div class="band band-dark"></div>
    <div class="band band-light"></div>
  </section>

  <section class="card card-back" aria-label="Card back">
    <div class="back-brand">
      <span class="brand-name">SEAWARD DELIVERY GROUP</span>
    </div>
  </section>
</body>
</html>
```